Patent Law

Need to develop a home page for a patent lawyer.

Colors should go with logo, blues...

Company Name- Corvel Tindry, PLLC

Company Overview-

I am an Intellectual Property Lawyer and focus on patents, copyrights, trademarks, & trade secrets. I work with small businesses and start ups in the chemical and biotech industries.

Why Us-

I am small firm that can provide large-firm service at a reasonable price. I also can charge flat-fees for entreprenuers in certain practice areas.

Services-
Intellectual Property
Patents
Copyrights
Trademarks
Trade secrets
Healthcare Compliance
Elder law
Wills
Trusts

Website we like-
http://www.quarnlowtide.example/ - within industry!!
http://www.vopperhask.example/
http://dulbrickovan.example/
http://thefernwoldguides.example/

Target Market(s)

My customers will be small business, specifically small start-up companies in the chemical and biotech arena.

Industry/Entity Type

Trade

Requirements
Must have
• Colors should go with logo, blues...

```html
<!DOCTYPE html>
<html lang="en">
<head>
<meta charset="utf-8">
<title>Corvel Tindry, PLLC — Patent &amp; Intellectual Property Law</title>
<link rel="stylesheet" href="https://fonts.googleapis.com/css2?family=PT+Sans+Narrow:wght@400;700&family=Arimo:ital,wght@0,400;0,700;1,400&family=Cinzel:wght@500&display=swap">
<style>
  :root{
    --brand-blue:#2a8db5;
    --ink:#222;
    --topbar:#151515;
    --footer:#1f1f1f;
    --footer-text:#d0d0d0;
    --footer-strong:#e6e6e6;
    --band-grey:#e7e7e7;
    --subscribe-bg:#f3f3f3;
    --rule:#e2e2e2;
  }
  *{box-sizing:border-box;margin:0;padding:0}
  html,body{width:900px;height:1200px;overflow:hidden;background:#fff}
  body{position:relative;font-family:"Arimo",Arial,sans-serif;color:var(--ink)}
  h1,h2,h3{font-weight:400}
  .abs{position:absolute}

  /* top bar */
  .topbar{left:0;top:0;width:900px;height:43px;background:var(--topbar)}
  .topbar-contact{right:44px;top:13px;color:#eee;font-size:12.5px;display:flex;align-items:center;gap:6px}
  .topbar-contact .sep{color:#777;margin:0 3px}

  /* header */
  .site-header{left:0;top:43px;width:900px;height:154px;background:linear-gradient(#fafafa,#ececec)}
  .brand{left:92px;top:164px;display:flex;align-items:center;gap:8px;font-family:"Cinzel",serif;font-weight:500;font-size:20px;color:#3a3f4a;letter-spacing:.5px}
  .brand-mark{width:14px;height:14px;border-radius:50%;background:var(--brand-blue)}
  .social{left:774px;top:72px;display:flex;gap:13px}
  .social span{width:19px;height:17px;background:#6f6f6f;border-radius:2px}
  .main-nav{left:352px;top:106px;display:flex;height:81px}
  .main-nav a{width:101px;height:81px;display:flex;align-items:center;justify-content:center;background:linear-gradient(#3a3a3a,#242424);color:#fff;text-decoration:none;font-family:"PT Sans Narrow",sans-serif;font-size:19px;font-weight:700;border-left:1px solid #555}
  .main-nav a.active{background:var(--brand-blue);font-weight:400;font-size:16px;border-left:none}

  /* hero */
  .hero-band{left:0;top:197px;width:900px;height:397px;background:var(--band-grey)}
  .hero{left:44px;top:206px;width:814px;height:376px;background:var(--brand-blue)}
  .hero-title{left:44px;top:314px;width:286px;text-align:center;color:#fff;font-family:"PT Sans Narrow",sans-serif;font-weight:400;line-height:1}
  .hero-title .l1{font-size:25px;display:block}
  .hero-title .l2{font-size:23px;font-weight:700;display:block;margin-top:11px}
  .hero-title .l2 small{font-size:14px;font-weight:400}
  .hero-title .l3{font-size:16.5px;display:block;margin-top:12px}
  .hero-btn{left:96px;top:437px;width:146px;height:44px;background:linear-gradient(#fff,#e9e9e9);display:flex;align-items:center;justify-content:center;font-family:"PT Sans Narrow",sans-serif;font-size:19px;color:#222;border-radius:2px}
  .hero-frame{left:354px;top:219px;width:492px;height:349px;background:#fff}
  .hero-photo{left:360px;top:225px;width:480px;height:337px;background:linear-gradient(135deg,#2f5fa8 0%,#9cc0df 35%,#e9e4df 60%,#c9d3df 100%)}
  .slide-arrow{top:550px;font-size:11px;font-weight:700;color:#222}

  /* subscribe */
  .subscribe{left:0;top:594px;width:900px;height:64px;background:var(--subscribe-bg)}
  .subscribe-icon{left:44px;top:614px}
  .subscribe-label{left:92px;top:621px;font-size:15.5px;color:#222;letter-spacing:.2px}
  .subscribe-input{left:524px;top:614px;width:229px;height:31px;background:#fff;border:1px solid #ddd}
  .subscribe-btn{left:753px;top:614px;width:104px;height:31px;background:var(--brand-blue);color:#fff;font-size:15.5px;display:flex;align-items:center;justify-content:center}

  /* services */
  .services-title{left:45px;top:702px;font-size:26px;color:#222}
  .services-arrows{left:280px;top:713px;display:flex;gap:2px}
  .services-arrows span{width:13px;height:12px;background:#555;border-radius:1px}
  .services-list{left:44px;top:740px;width:265px;list-style:none;border-top:2px solid var(--rule)}
  .services-list li{height:31px;border-bottom:2px solid var(--rule);display:flex;align-items:center;gap:9px;padding-left:14px;font-style:italic;font-size:12.5px;color:#333}
  .services-list li:last-child{border-bottom:none}
  .bullet{width:16px;height:16px;border-radius:50%;background:#333;display:flex;align-items:center;justify-content:center}

  /* why us */
  .why-photo{left:352px;top:708px;width:172px;height:182px;background:linear-gradient(90deg,#4b5566 0%,#c7c4c2 40%,#e8dcd0 60%,#2a2f3a 100%)}
  .why-title{left:540px;top:708px;font-size:31px;font-weight:700;color:var(--brand-blue)}
  .why-sub{left:540px;top:747px;font-size:18px;color:#333}
  .why-lead{left:540px;top:791px;width:320px;font-size:11.7px;font-weight:700;line-height:15.5px;color:#222}
  .why-body{left:540px;top:853px;width:320px;font-size:11.5px;line-height:15.5px;color:#333}
  .read-more{left:352px;top:913px;display:flex;align-items:center;gap:7px;font-size:14.5px;color:#222}

  /* footer */
  .footer-rule{left:0;top:999px;width:900px;height:6px;background:#cfcfcf}
  .site-footer{left:0;top:1005px;width:900px;height:195px;background:var(--footer)}
  .footer-heading{top:1040px;font-size:18px;font-weight:400;color:var(--footer-strong)}
  .footer-links{top:1072px;list-style:none;font-size:12px;line-height:24px;color:var(--footer-text)}
  .footer-links li::before{content:"›";color:var(--brand-blue);margin-right:7px}
  .footer-links b{color:var(--footer-strong)}
  .testimonial{left:592px;top:1068px;width:262px;font-size:12px;line-height:15.5px;font-style:italic;color:var(--footer-text)}
  .testimonial .who{color:var(--brand-blue);font-weight:700}
  .testimonial .more{display:block;margin-top:7px;font-size:11.5px}
  .copyright{left:44px;top:1173px;font-size:11px;color:var(--footer-strong)}
  .copyright .name{color:var(--brand-blue)}
  .copyright u{color:var(--footer-strong)}
</style>
</head>
<body>

<div class="abs topbar"></div>
<div class="abs topbar-contact">
  <svg width="8" height="12" viewBox="0 0 8 12"><rect x="0.5" y="0.5" width="7" height="11" rx="1" fill="#ccc"/><rect x="2" y="2" width="4" height="6" fill="#333"/></svg>
  <span>1(800) 555-0142</span><span class="sep">|</span><span>MAP</span>
</div>

<header class="abs site-header"></header>
<div class="abs brand"><span class="brand-mark"></span>CORVEL TINDRY, PLLC</div>
<div class="abs social"><span></span><span></span><span></span></div>
<nav class="abs main-nav">
  <a class="active">HOME</a><a>Practice</a><a>Services</a><a>Resources</a><a>Contacts</a>
</nav>

<div class="abs hero-band"></div>
<section class="abs hero"></section>
<h1 class="abs hero-title">
  <span class="l1">REALIZE YOUR</span>
  <span class="l2">CONSTITUTIONAL <small>RIGHT</small></span>
  <span class="l3">WITH QUALIFIED HELP</span>
</h1>
<div class="abs hero-btn">READ MORE</div>
<div class="abs hero-frame"></div>
<div class="abs hero-photo" role="img" aria-label="Photo of hands holding pens over a printed document beside a keyboard"></div>
<span class="abs slide-arrow" style="left:361px">«</span>
<span class="abs slide-arrow" style="left:830px">»</span>

<section class="abs subscribe"></section>
<svg class="abs subscribe-icon" width="38" height="28" viewBox="0 0 38 28"><rect x="1" y="1" width="36" height="26" fill="none" stroke="#222" stroke-width="2"/><path d="M1 1 L19 16 L37 1 M1 27 L14 12 M37 27 L24 12" fill="none" stroke="#222" stroke-width="2"/></svg>
<div class="abs subscribe-label">KEEP UP TO DATE ON THE LATEST FROM OUR CASES:</div>
<div class="abs subscribe-input"></div>
<div class="abs subscribe-btn">SUBSCRIBE</div>

<h2 class="abs services-title">Our Services</h2>
<div class="abs services-arrows"><span></span><span></span></div>
<ul class="abs services-list">
  <li><span class="bullet"><svg width="8" height="6" viewBox="0 0 8 6"><path d="M0 3H7M4.5 0.5L7 3L4.5 5.5" stroke="#fff" fill="none" stroke-width="1.2"/></svg></span>Intellectual Property</li>
  <li><span class="bullet"><svg width="8" height="6" viewBox="0 0 8 6"><path d="M0 3H7M4.5 0.5L7 3L4.5 5.5" stroke="#fff" fill="none" stroke-width="1.2"/></svg></span>Patents</li>
  <li><span class="bullet"><svg width="8" height="6" viewBox="0 0 8 6"><path d="M0 3H7M4.5 0.5L7 3L4.5 5.5" stroke="#fff" fill="none" stroke-width="1.2"/></svg></span>Copyrights</li>
  <li><span class="bullet"><svg width="8" height="6" viewBox="0 0 8 6"><path d="M0 3H7M4.5 0.5L7 3L4.5 5.5" stroke="#fff" fill="none" stroke-width="1.2"/></svg></span>Trademarks</li>
  <li><span class="bullet"><svg width="8" height="6" viewBox="0 0 8 6"><path d="M0 3H7M4.5 0.5L7 3L4.5 5.5" stroke="#fff" fill="none" stroke-width="1.2"/></svg></span>Trade secrets</li>
  <li><span class="bullet"><svg width="8" height="6" viewBox="0 0 8 6"><path d="M0 3H7M4.5 0.5L7 3L4.5 5.5" stroke="#fff" fill="none" stroke-width="1.2"/></svg></span>Healthcare Compliance</li>
  <li><span class="bullet"><svg width="8" height="6" viewBox="0 0 8 6"><path d="M0 3H7M4.5 0.5L7 3L4.5 5.5" stroke="#fff" fill="none" stroke-width="1.2"/></svg></span>Elder law</li>
</ul>

<div class="abs why-photo" role="img" aria-label="Portrait photo of a smiling attorney in a dark business suit"></div>
<h2 class="abs why-title">Why us?</h2>
<p class="abs why-sub">We hold the national quality standard.</p>
<p class="abs why-lead">Lorem ipsum dolor sit amet, consectetur adipisicig elit, sed do eiusmod tempor incididunt labore et doloagna astum aliqua.</p>
<p class="abs why-body">Uenim ad minim veniam, quis nostrud laboris nisi utaliquip ex ea commodoconsequat. Duisute irurdolor into reprehenderitin voluptate velit esse cillum.</p>
<div class="abs read-more"><span class="bullet" style="width:14px;height:14px"><svg width="6" height="6" viewBox="0 0 6 6"><path d="M1 0.5L4 3L1 5.5M3 0.5L6 3L3 5.5" stroke="#fff" fill="none"/></svg></span>read more</div>

<div class="abs footer-rule"></div>
<footer class="abs site-footer"></footer>
<h3 class="abs footer-heading" style="left:44px">Links</h3>
<ul class="abs footer-links" style="left:44px"><li>Home</li><li>About us</li><li>Our Services</li></ul>
<ul class="abs footer-links" style="left:180px"><li>Practice</li><li>Resources</li><li>Contact us</li></ul>
<h3 class="abs footer-heading" style="left:351px">Contact info</h3>
<ul class="abs footer-links" style="left:351px"><li><b>Add :</b> 4150, Lorem, Ipsum 400.</li><li><b>Mob :</b> 1(800)555-0142</li><li><b>Mail :</b> info@corveltindry.example</li></ul>
<h3 class="abs footer-heading" style="left:592px">Testimonials</h3>
<div class="abs testimonial">
  “Mam libero tempore massasoluta nobis est eligendi omnis voluasassumenda est, omnis doloresereeledusempquibusdamet aurerum odes massa laoreetum est...”<br>
  <span class="who">mr. Rowan Ellery</span><br>(New York)<br><span class="more">View All »</span>
</div>
<div class="abs copyright"><span class="name">CORVEL TINDRY, PLLC</span> © 2014 &nbsp;|&nbsp; <u>Privacy policy</u></div>

</body>
</html>
```